Rising Paths Web Design

I am starting a new company that will provide LIFE COACHING services - I have tried to design a website, but it's too complicated. Right now, it's just me - I'm the only person that will provide services through the website - I have used artmarket to purchase a logo (see below). I want to be able to update the website myself, but need a template - basic design. Because I am not technologically savvy enough to explain in words - I basically want to have a website that will provide basic information about my services (coaching), a page about me and my background, hopefully scheduling possibilities, and testimonials — also a page for writing/blogs. I bought a website through NetHarbor - so when I have a template, I guess I”d use that - but maybe I’ll need to work with a designer to actually get it up on the internet. I have a head shot that I’ll upload, too.
Target Market(s)
Clients from the independent (private school) world - teachers, administrators
Number of Pages Required
4 page
Look and feel
Each slider illustrates characteristics of the customer's brand and the style your logo design should communicate.

```html
<!DOCTYPE html>
<html lang="en">
<head>
<meta charset="utf-8">
<title>Rising Paths Coaching</title>
<link href="https://fonts.googleapis.com/css2?family=Cinzel:wght@400;600&family=Rubik:wght@400;500&display=swap" rel="stylesheet">
<style>
:root{
  --teal:#00a396;
  --teal-light:#2fb8ad;
  --ink:#2f2f2f;
  --text:#555;
  --muted:#777;
  --footer:#414042;
  --white:#fff;
}
*{margin:0;padding:0;box-sizing:border-box}
html,body{width:1200px;height:3656px;overflow:hidden;background:var(--white)}
body{position:relative;font-family:'Rubik',sans-serif;color:var(--text)}
.abs{position:absolute}
.serif{font-family:'Cinzel',serif;color:var(--ink)}
.logo-ring{border:2px solid var(--teal);border-radius:50%}
.logo-name{font-family:'Cinzel',serif;color:#3a3a3a;font-size:19px}
.nav{top:35px;left:543px;font-size:13px;color:#333}
.nav a{position:absolute;white-space:nowrap;text-decoration:none;color:#333}
.nav a.active{color:var(--teal)}
.btn-outline{border:2px solid var(--teal);color:#333;font-size:13px;display:flex;align-items:center;justify-content:center}
.btn-solid{background:var(--teal);color:var(--white);font-size:13px;font-weight:500;display:flex;align-items:center;justify-content:center}
.photo{background:linear-gradient(135deg,#e8ecea,#b9b6b0 55%,#8e8680)}
.card{background:var(--white);box-shadow:0 6px 22px rgba(0,0,0,.08)}
.card-title{font-family:'Cinzel',serif;font-size:22px;color:#333;font-weight:400}
.card-text{font-size:14px;line-height:21px;color:var(--muted)}
.link{color:var(--teal);font-size:13.5px;font-weight:500}
.mini-body{position:absolute;left:269px;width:215px;display:flex;flex-direction:column}
.mini-body .date{font-size:13px;color:#555}
.mini-body .card-title{margin-top:4px;line-height:26px}
.mini-body .card-text{font-size:13px;line-height:21px;margin-top:2px}
.mini-body .link{margin-top:7px}
.mini-body.on-teal .date,.mini-body.on-teal .card-title,.mini-body.on-teal .card-text,.mini-body.on-teal .link{color:var(--white)}
.section-title{font-family:'Cinzel',serif;color:#333;text-align:center;width:1200px;left:0;font-weight:400}
.foot-title{font-family:'Cinzel',serif;color:var(--white);font-size:21px}
.foot-text{color:var(--white);font-size:13px}
</style>
</head>
<body>

<!-- Header -->
<div class="abs logo-ring" style="left:88px;top:12px;width:22px;height:22px"></div>
<div class="abs logo-name" style="left:88px;top:58px;width:175px">Rising Paths</div>

<nav class="abs nav">
  <a class="active" style="left:0">HOME</a>
  <a style="left:67px">ABOUT ME</a>
  <a style="left:159px">SERVICES</a>
  <a style="left:247px">BLOGS</a>
  <a style="left:316px">CONTACT US</a>
</nav>
<div class="abs btn-outline" style="left:962px;top:24px;width:148px;height:41px">SCHEDULE NOW</div>

<!-- Hero -->
<div class="abs photo" role="img" aria-label="Group of adults seated in a bright room taking notes during a coaching session" style="left:679px;top:85px;width:521px;height:650px;background:linear-gradient(160deg,#f2f3f2,#cfd2cf 40%,#8a7f78 75%,#5b5550)"></div>
<div class="abs serif" style="left:88px;top:300px;font-size:27px;color:#555;letter-spacing:.5px">LIFE COACHING SERVICES</div>
<div class="abs" style="left:117px;top:346px;width:2px;height:112px;background:var(--teal)"></div>
<div class="abs serif" style="left:135px;top:345px;font-size:55px;line-height:56px;font-weight:400;color:#333">RISING PATHS<br>COACHING</div>
<div class="abs" style="left:137px;top:463px;width:420px;font-size:16px;line-height:22px;color:#555">Life coaching is a coaching niche that is tremendously growing with time.</div>
<div class="abs btn-solid" style="left:138px;top:519px;width:149px;height:42px">SCHEDULE NOW</div>

<!-- About -->
<svg class="abs" style="left:140px;top:780px" width="280" height="300" viewBox="0 0 280 300" aria-hidden="true">
  <path d="M190 30 A200 200 0 0 0 90 250" fill="none" stroke="var(--teal)" stroke-width="2"/>
</svg>
<div class="abs" style="left:225px;top:855px;width:400px;height:400px;border-radius:50%;box-shadow:0 30px 60px rgba(0,0,0,.12)"></div>
<div class="abs" role="img" aria-label="Head shot of the coach, a smiling woman with short blonde hair in a kitchen" style="left:225px;top:855px;width:400px;height:400px;border-radius:50%;background:radial-gradient(circle at 50% 45%,#d9b99a,#a88c74 45%,#7e756c 80%)"></div>
<div class="abs serif" style="left:681px;top:930px;font-size:50px;color:#333">ABOUT ME</div>
<div class="abs" style="left:682px;top:996px;width:380px;font-size:14.5px;line-height:21.3px;color:#555">Lorem Ipsum is simply dummy text of the printing and typesetting industry. Lorem Ipsum has been the industry's standard dummy text ever since the 1500s, when an unknown printer took a galley of type and scrambled it to make a type specimen book. It has survived not only five centuries, but also the leap into electronic typesetting, remaining .</div>
<div class="abs btn-outline" style="left:682px;top:1161px;width:120px;height:41px">READ MORE</div>

<!-- Services -->
<div class="abs section-title" style="top:1372px;font-size:52px">OUR SERVICES</div>
<div class="abs" style="left:0;top:1795px;width:1200px;height:520px;background:var(--teal)"></div>

<div class="abs card" style="left:140px;top:1459px;width:298px;height:380px">
  <div class="photo" role="img" aria-label="Workshop audience facing a presenter in a bright room" style="height:201px;background:linear-gradient(160deg,#e9ece8,#b2aea6 55%,#6d655d)"></div>
  <div class="abs card-title" style="left:31px;top:228px">LIFE COACHING</div>
  <div class="abs card-text" style="left:31px;top:261px;width:250px">Lorem Ipsum is simply dummy text of the printing and typesetting industry. Lorem Ipsum has been.</div>
  <div class="abs link" style="left:31px;top:333px">READ MORE</div>
</div>
<div class="abs card" style="left:451px;top:1459px;width:298px;height:380px">
  <div class="photo" role="img" aria-label="Small group of adults talking in a circle of chairs" style="height:201px;background:linear-gradient(160deg,#dcdcdc,#8d8780 55%,#4e4541)"></div>
  <div class="abs card-title" style="left:29px;top:228px">HEALTH COACHING</div>
  <div class="abs card-text" style="left:29px;top:261px;width:250px">Lorem Ipsum is simply dummy text of the printing and typesetting industry. Lorem Ipsum has been.</div>
  <div class="abs link" style="left:29px;top:333px">READ MORE</div>
</div>
<div class="abs card" style="left:761px;top:1459px;width:298px;height:380px">
  <div class="photo" role="img" aria-label="Group discussion seated by large windows" style="height:197px;background:linear-gradient(160deg,#eef0ee,#b7b3ad 55%,#6f6862)"></div>
  <div class="abs card-title" style="left:29px;top:228px">CAREER COACHING</div>
  <div class="abs card-text" style="left:29px;top:261px;width:250px">Lorem Ipsum is simply dummy text of the printing and typesetting industry. Lorem Ipsum has been.</div>
  <div class="abs link" style="left:29px;top:333px">READ MORE</div>
</div>

<!-- Testimonials -->
<div class="abs" style="left:0;top:1895px;width:1200px;text-align:center;font-family:Georgia,serif;font-size:170px;line-height:170px;color:var(--teal-light)">&ldquo;</div>
<div class="abs section-title" style="top:2014px;font-size:53px;color:var(--white)">TESTIMONIALS</div>
<div class="abs" style="left:280px;top:2082px;width:640px;text-align:center;font-size:14.5px;line-height:21.3px;color:var(--white)">Lorem Ipsum is simply dummy text of the printing and typesetting industry. Lorem Ipsum has been the industry's standard dummy text ever since the 1500s, when an unknown printer took a galley of type and scrambled it to make a type specimen book.</div>
<div class="abs" role="img" aria-label="Portrait of the client giving the testimonial" style="left:522px;top:2157px;width:50px;height:50px;border-radius:50%;background:radial-gradient(circle,#d8cfc6,#9c9289);border:2px solid var(--white)"></div>
<div class="abs" style="left:584px;top:2164px;font-size:17px;font-weight:500;color:var(--white)">Mark Ellison</div>
<div class="abs" style="left:584px;top:2186px;font-size:12px;color:var(--white)">Co Founder</div>

<!-- Blog -->
<div class="abs section-title" style="top:2423px;font-size:52px">LATEST BLOG</div>

<div class="abs card" style="left:88px;top:2514px;width:512px;height:428px">
  <div class="photo" role="img" aria-label="Business team seated in a circle during a meeting" style="height:288px;background:linear-gradient(160deg,#f0f1f0,#bdb9b2 45%,#4a4644)"></div>
  <div class="abs" style="left:42px;top:313px;font-size:13px;color:#555">05-Apr-2022</div>
  <div class="abs card-title" style="left:42px;top:333px">BLOG HEADING HERE</div>
  <div class="abs card-text" style="left:42px;top:363px;width:450px">Lorem Ipsum is simply dummy text of the printing and typesetting industry. Lorem Ipsum has been.</div>
</div>

<div class="abs card" style="left:613px;top:2514px;width:497px;height:206px">
  <div class="photo abs" role="img" aria-label="Audience raising hands at a seminar" style="left:0;top:0;width:232px;height:206px;background:linear-gradient(160deg,#e6e9e6,#a39e96 55%,#5a524c)"></div>
  <div class="mini-body" style="top:36px">
    <div class="date">05-Apr-2022</div>
    <div class="card-title">BLOG HEADING</div>
    <div class="card-text">Lorem Ipsum is simply dummy text of the printing and typeset- ting industry lorem ipsum.</div>
    <div class="link">READ MORE</div>
  </div>
</div>

<div class="abs" style="left:613px;top:2737px;width:497px;height:205px;background:var(--teal)">
  <div class="photo abs" role="img" aria-label="Presenter at a flip chart in front of an office team" style="left:0;top:0;width:233px;height:205px;background:linear-gradient(160deg,#f1f2f1,#c6c0b8 50%,#8b5a52)"></div>
  <div class="mini-body on-teal" style="top:38px">
    <div class="date">05-Apr-2022</div>
    <div class="card-title">BLOG HEADING</div>
    <div class="card-text">Lorem Ipsum is simply dummy text of the printing and typeset- ting industry lorem ipsum.</div>
    <div class="link">READ MORE</div>
  </div>
</div>

<!-- Credentials -->
<div class="abs" style="left:400px;top:3039px;width:99px;height:99px;border-radius:8px;background:#1d5f86"></div>
<div class="abs" style="left:549px;top:3039px;width:98px;height:99px;border-radius:8px;background:#1f4f7a"></div>
<div class="abs" style="left:700px;top:3039px;width:98px;height:98px;border-radius:50%;border:6px solid #1aa0d8;background:var(--white)"></div>

<!-- Footer -->
<footer class="abs" style="left:0;top:3216px;width:1200px;height:440px;background:var(--footer)"></footer>
<div class="abs logo-ring" style="left:125px;top:3388px;width:22px;height:22px"></div>
<div class="abs logo-name" style="left:133px;top:3420px;color:var(--white);font-size:20px">Rising Paths</div>

<div class="abs foot-title" style="left:404px;top:3339px">USEFUL LINKS</div>
<div class="abs foot-text" style="left:406px;top:3375px;line-height:27px">Home<br>About Me<br>Services<br>Blogs<br>Contact Us</div>

<div class="abs foot-title" style="left:622px;top:3339px">NEWSLETTER</div>
<div class="abs foot-text" style="left:622px;top:3377px">Subscribe to our newsletter</div>
<div class="abs" style="left:622px;top:3405px;width:205px;height:37px;background:#5a595b;color:#ccc;font-size:12px;padding:11px 18px">Email Address</div>
<div class="abs btn-solid" style="left:622px;top:3449px;width:120px;height:35px">SUBSCRIBE</div>

<div class="abs foot-title" style="left:900px;top:3339px">CONTACT US</div>
<svg class="abs" style="left:900px;top:3377px" width="12" height="70" viewBox="0 0 12 70" aria-hidden="true">
  <path d="M6 1a4.5 4.5 0 0 0-4.5 4.5C1.5 9 6 13 6 13s4.5-4 4.5-7.5A4.5 4.5 0 0 0 6 1z" fill="var(--teal)"/>
  <rect x="1" y="27" width="10" height="8" rx="1" fill="var(--teal)"/>
  <path d="M2 50c1 4 4 7 8 8l1.5-2-2.5-1.5-1 1c-1.5-.7-2.8-2-3.5-3.5l1-1L4 48.5z" fill="var(--teal)"/>
</svg>
<div class="abs foot-text" style="left:918px;top:3377px;line-height:24px">Some goes address here<br>hello@risingpaths.com<br>+1 555 014 22</div>
<div class="abs" style="left:900px;top:3461px;display:flex;gap:14px">
  <span style="width:11px;height:11px;border-radius:50%;background:var(--white)"></span>
  <span style="width:11px;height:11px;border-radius:50%;background:var(--white)"></span>
  <span style="width:11px;height:11px;border-radius:50%;background:var(--white)"></span>
  <span style="width:11px;height:11px;border-radius:50%;background:var(--white)"></span>
</div>

<div class="abs" style="left:88px;top:3599px;width:1022px;height:1px;background:#6b6a6c"></div>
<div class="abs foot-text" style="left:0;top:3618px;width:1200px;text-align:center;font-size:14px">©Copyright 2022 | All Rights Reserved</div>
<div class="abs" style="left:1132px;top:3579px;width:40px;height:40px;border-radius:50%;background:var(--teal)">
  <svg width="40" height="40" viewBox="0 0 40 40" aria-hidden="true"><path d="M16 22l4-4 4 4" fill="none" stroke="#fff" stroke-width="2"/></svg>
</div>

</body>
</html>
```